Property inspection company needs logo/business card design

A new, home, commercial, and multi dwelling inspection company needs help with a new logo and hence business cards.

Time is extended for the rest of the week.

Font styles to use
Sans Serif

Colors
ec1f27
0255a3
ffffff

```html
<!DOCTYPE html>
<html lang="en">
<head>
<meta charset="utf-8">
<title>Ray Calloway Property Inspections – Business Card</title>
<link href="https://fonts.googleapis.com/css2?family=Roboto:wght@400;500;700&display=swap" rel="stylesheet">
<style>
  :root {
    --brand-red: #ec1f27;
    --brand-blue: #0255a3;
    --blue-light: #2f8fd6;
    --white: #ffffff;
    --page: #e9ebee;
  }
  * { margin: 0; padding: 0; box-sizing: border-box; }
  html, body {
    width: 1200px; height: 780px; overflow: hidden;
    background: var(--page);
    font-family: "Roboto", Arial, sans-serif;
  }
  .card {
    position: absolute; left: 75px; top: 90px;
    width: 1050px; height: 600px;
    border-radius: 28px; overflow: hidden;
    background: var(--white);
    box-shadow: 0 10px 30px rgba(0,0,0,.18);
  }
  .card-wave { position: absolute; inset: 0; width: 100%; height: 100%; }
  .brand {
    position: absolute; left: 90px; top: 150px;
    display: flex; align-items: flex-start; gap: 18px;
  }
  .brand-mark {
    width: 26px; height: 26px; margin-top: 14px;
    background: var(--brand-blue);
  }
  .brand-name {
    color: var(--brand-red); font-weight: 700;
    font-size: 56px; line-height: 1.05; letter-spacing: .5px;
    text-transform: uppercase;
  }
  .brand-name .brand-sub { display: block; font-size: 22px; letter-spacing: 5px; margin-top: 10px; }
  .contact {
    position: absolute; left: 340px; top: 430px; color: var(--white);
  }
  .contact-name { font-size: 27px; font-weight: 700; letter-spacing: .5px; text-transform: uppercase; }
  .contact-role { font-size: 22px; margin-bottom: 16px; }
  .contact-line { display: flex; align-items: center; gap: 12px; font-size: 22px; margin-top: 6px; }
  .contact-line svg { width: 18px; height: 18px; flex: none; }
  .address {
    position: absolute; right: 60px; top: 210px;
    color: var(--white); font-size: 24px; line-height: 1.4; text-align: right;
  }
</style>
</head>
<body>
  <section class="card">
    <svg class="card-wave" viewBox="0 0 1050 600" preserveAspectRatio="none" aria-hidden="true">
      <defs>
        <linearGradient id="blueField" x1="0" y1="1" x2="1" y2="0">
          <stop offset="0" stop-color="var(--blue-light)"/>
          <stop offset="1" stop-color="var(--brand-blue)"/>
        </linearGradient>
      </defs>
      <path class="wave-red" fill="var(--brand-red)"
        d="M740,0 C800,40 780,110 680,190 C540,300 290,355 0,350 L0,600 L1050,600 L1050,0 Z"/>
      <path class="wave-blue" fill="url(#blueField)" stroke="var(--white)" stroke-width="5"
        d="M790,-4 C850,45 830,125 720,215 C575,330 320,385 -4,385 L-4,604 L1054,604 L1054,-4 Z"/>
    </svg>

    <div class="brand">
      <span class="brand-mark"></span>
      <p class="brand-name">Ray Calloway<span class="brand-sub">Property Inspections Inc</span></p>
    </div>

    <div class="contact">
      <p class="contact-name">Dana Mercer</p>
      <p class="contact-role">Director</p>
      <p class="contact-line">
        <svg viewBox="0 0 18 18"><rect x="2" y="2" width="14" height="14" fill="none" stroke="var(--white)" stroke-width="2"/></svg>
        (555) 014 2290
      </p>
      <p class="contact-line">
        <svg viewBox="0 0 18 18"><rect x="1" y="3" width="16" height="12" fill="var(--white)"/><path d="M1,3 L9,10 L17,3" fill="none" stroke="var(--brand-blue)" stroke-width="1.5"/></svg>
        hello@callowayinspect.com
      </p>
    </div>

    <p class="address">PO BOX 480, Mesa Court<br>4th Lane, Arizona</p>
  </section>
</body>
</html>
```